Selka Varon Photography

I need a website design for my photography business, I want something clean, elegant, Classy.. I like the colors, White, Black, Green/Blue, Pink, Brown, Lavender,, I have a lot added my Logo .... Additional Info... I need a Photography Website Design, with probably 6 Tabs, Home, About Me, Portfolio, Gallery, Investment, Contact.
Home Page should have my logo, Name & Address, Social Media Icons, and Pictures.
As long as the templates are made I have a hosting coming that will code it.
Portraits Photography, Senior Portraits, Newborn, Families, Events, Engagements, Wedding,
Business
5+ page

```html
<!DOCTYPE html>
<html lang="en">
<head>
<meta charset="utf-8">
<title>Selka Varon Photography</title>
<link href="https://fonts.googleapis.com/css2?family=Open+Sans:ital,wght@0,300;0,400;0,600;1,400&family=Arimo:wght@400;700&display=swap" rel="stylesheet">
<style>
:root{
  --page:#2b2b2b;
  --page-dark:#1d1d1d;
  --bar:#0a0a0a;
  --panel:#111112;
  --pink:#ef5fae;
  --teal:#4ccfb3;
  --heading:#a9a9a9;
  --text:#8a8a8a;
  --text-light:#e4e4e4;
  --frame:#f4f4f4;
}
*{margin:0;padding:0;box-sizing:border-box}
html,body{width:1176px;height:1200px;overflow:hidden}
body{background:radial-gradient(ellipse at 50% 20%,#343434 0%,var(--page) 40%,var(--page-dark) 100%);font-family:"Open Sans",sans-serif;color:var(--text);position:relative}
.abs{position:absolute}

/* header */
.topbar{left:0;top:0;width:1176px;height:54px;background:linear-gradient(#141414,var(--bar));border-bottom:1px solid #000;box-shadow:0 2px 6px rgba(0,0,0,.6)}
.nav a{position:absolute;top:21px;font-family:"Arimo",sans-serif;font-size:11.5px;font-weight:700;letter-spacing:.3px;color:#cfcfcf;text-decoration:none;white-space:nowrap}
.brand{left:468px;top:0;width:222px;height:54px;display:flex;align-items:center;justify-content:center;gap:8px}
.brand-mark{width:10px;height:10px;background:var(--pink)}
.brand-name{font-family:"Open Sans",sans-serif;font-weight:400;font-size:16px;color:var(--pink);white-space:nowrap}

/* slider */
.slider{left:89px;top:138px;width:997px;height:548px;background:var(--panel);border-radius:3px}
.slide-frame{left:103px;top:151px;width:972px;height:377px;background:linear-gradient(90deg,#ffffff,#dcdcdc 6%,#dcdcdc 94%,#ffffff)}
.slide-photo{left:157px;top:151px;width:864px;height:377px;background:linear-gradient(100deg,#6f7a2c 0%,#3f5a26 35%,#2c3d1c 55%,#5b3b2a 72%,#3a2a22 100%)}
.caption{left:157px;top:424px;width:864px;height:104px;background:rgba(10,10,10,.72);padding:15px 18px}
.caption h2{font-weight:400;font-size:21px;color:#fff;margin-bottom:11px}
.caption p{font-size:13.5px;line-height:17px;color:#9a9a9a;letter-spacing:.2px}
.arrow{top:324px}
.thumb{top:564px;width:95px;height:94px;background:var(--frame);padding:6px;border-radius:2px;box-shadow:0 2px 4px rgba(0,0,0,.6)}
.thumb div{width:100%;height:100%}
.thumb.active{top:558px}
.caret{left:212px;top:548px}

/* content panels */
.panel{background:var(--panel);border-radius:2px}
.main-panel{left:90px;top:703px;width:726px;height:384px}
.side-panel{left:835px;top:703px;width:249px;height:384px}
.section-title{font-weight:300;font-size:20px;color:var(--heading);letter-spacing:-.3px}
.divider{left:401px;top:739px;width:2px;height:308px;background:#2a2a2b}
.post-img{left:113px;width:77px;height:69px}
.post-title{left:205px;font-size:10px;color:var(--pink);letter-spacing:-.2px}
.post-text{left:205px;font-size:9.5px;line-height:16px;color:#9a9a9a}
.post-date{left:205px;font-size:9.5px;font-style:italic;color:var(--teal)}
.post-rule{left:113px;width:249px;height:1px;background:#252526}
.body-copy{font-size:12px;line-height:22px;color:var(--text)}
.body-copy strong{font-weight:400;color:var(--text-light)}
.bullet{width:6px;height:6px;border-radius:50%;background:var(--teal)}
.teal-link{font-size:12px;color:var(--teal)}
.read-more{font-size:12px;color:var(--teal);text-decoration:underline}
.photo-frame{left:444px;top:907px;width:95px;height:94px;background:var(--frame);padding:5px;border-radius:2px}
.photo-frame div{width:100%;height:100%;background:linear-gradient(135deg,#3b2f2a,#b48268 60%,#d9c0a8)}
.links li{list-style:none;position:absolute;left:0;font-size:12px;color:var(--text);white-space:nowrap}
.links li::before{content:"";position:absolute;left:-29px;top:7px;width:6px;height:6px;border-radius:50%;background:var(--teal)}

/* footer */
.footer{left:0;top:1102px;width:1176px;height:98px;background:#050505}
.foot-nav{left:90px;top:1136px;font-size:8.5px;color:#777;white-space:nowrap;word-spacing:2px}
.foot-nav span{margin:0 12px}
.copyright{left:90px;top:1160px;font-size:8.5px;color:#666}
.follow{left:832px;top:1149px;font-size:8px;color:#777}
.social{top:1138px;width:29px;height:29px;border-radius:50%;background:#2a2a2a;border:1px solid #333}
</style>
</head>
<body>

<header>
  <div class="abs topbar"></div>
  <nav class="nav">
    <a style="left:90px">HOME</a>
    <a style="left:194px">ABOUT ME</a>
    <a style="left:316px">PORTFOLIO</a>
    <a style="left:780px">GALLERY</a>
    <a style="left:894px">INVESTMENT</a>
    <a style="left:1029px">CONTACT</a>
  </nav>
  <div class="abs brand">
    <span class="brand-mark"></span>
    <span class="brand-name">Selka Varon Photography</span>
  </div>
</header>

<section class="abs slider"></section>
<div class="abs slide-frame"></div>
<div class="abs slide-photo" role="img" aria-label="Portrait of a woman blowing petals in a green garden"></div>
<div class="abs caption">
  <h2>Selka Varon Studio</h2>
  <p>Nullam pretium auctor massa ut consequat. Etiam hendrerit iaculis mattis. Proin tincidunt gravida augue in tempor. Proin blandit, elit a consectetur tincidunt, velit quam tristique risus, eget ultrices lorem dui ut nisl.</p>
</div>
<svg class="abs arrow" style="left:120px" width="22" height="30" viewBox="0 0 22 30"><path d="M16 3 L5 15 L16 27" fill="none" stroke="#444" stroke-width="4"/></svg>
<svg class="abs arrow" style="left:1036px" width="22" height="30" viewBox="0 0 22 30"><path d="M6 3 L17 15 L6 27" fill="none" stroke="#555" stroke-width="4"/></svg>

<svg class="abs caret" width="14" height="10" viewBox="0 0 14 10"><path d="M0 10 L7 2 L14 10Z" fill="#f4f4f4"/></svg>
<div class="abs thumb active" style="left:173px"><div role="img" aria-label="Woman blowing petals outdoors" style="background:linear-gradient(135deg,#6f8a3a,#3a4a24)"></div></div>
<div class="abs thumb" style="left:276px"><div role="img" aria-label="Friends jumping on a beach" style="background:linear-gradient(#9cc5e8,#c9b58d)"></div></div>
<div class="abs thumb" style="left:380px"><div role="img" aria-label="Couple with bicycles in a park" style="background:linear-gradient(135deg,#7a9a4a,#c8c0a0)"></div></div>
<div class="abs thumb" style="left:483px"><div role="img" aria-label="Friends at a garden party" style="background:linear-gradient(135deg,#a9b86a,#e2d7b8)"></div></div>
<div class="abs thumb" style="left:586px"><div role="img" aria-label="People dancing at a night party" style="background:linear-gradient(135deg,#2a1a3a,#8a2a4a)"></div></div>
<div class="abs thumb" style="left:690px"><div role="img" aria-label="Two women taking a photo" style="background:linear-gradient(135deg,#e8d8b8,#3aa090)"></div></div>
<div class="abs thumb" style="left:794px"><div role="img" aria-label="Family with a child on a beach" style="background:linear-gradient(#a8d0ea,#d8c8a0)"></div></div>
<div class="abs thumb" style="left:897px"><div role="img" aria-label="Group of friends giving thumbs up" style="background:linear-gradient(135deg,#7aaee0,#c88a6a)"></div></div>

<section class="abs panel main-panel"></section>
<section class="abs panel side-panel"></section>

<h3 class="abs section-title" style="left:112px;top:727px">LATEST BLOG</h3>
<div class="abs divider"></div>

<div class="abs post-img" style="top:784px" role="img" aria-label="Friends taking a selfie"><div style="width:100%;height:100%;background:linear-gradient(135deg,#8ac0c8,#d8a070)"></div></div>
<div class="abs post-title" style="top:783px">VARIOUS VERSIONS HAVE EVOLVED</div>
<div class="abs post-text" style="top:801px">Various versions have evolved over<br>the years, sometimes...</div>
<div class="abs post-date" style="top:837px">Upcoming &nbsp;29 &nbsp;Apr 2015</div>
<div class="abs post-rule" style="top:866px"></div>

<div class="abs post-img" style="top:880px" role="img" aria-label="Smiling woman portrait"><div style="width:100%;height:100%;background:linear-gradient(135deg,#5a3a2a,#d8b098 60%,#f0e8e0)"></div></div>
<div class="abs post-title" style="top:879px">VARIOUS VERSIONS HAVE EVOLVED</div>
<div class="abs post-text" style="top:897px">Various versions have evolved over<br>the years, sometimes...</div>
<div class="abs post-date" style="top:933px">Upcoming 29 Apr 2015</div>
<div class="abs post-rule" style="top:962px"></div>

<div class="abs post-img" style="top:976px" role="img" aria-label="Friends looking at a tablet"><div style="width:100%;height:100%;background:linear-gradient(135deg,#a0b8d0,#8a5a4a)"></div></div>
<div class="abs post-title" style="top:975px">VARIOUS VERSIONS HAVE EVOLVED</div>
<div class="abs post-text" style="top:993px">Various versions have evolved over<br>the years, sometimes...</div>
<div class="abs post-date" style="top:1029px">Upcoming 29 Apr 2015</div>

<h3 class="abs section-title" style="left:438px;top:727px">WELCOME TO MY PAGE</h3>
<p class="abs body-copy" style="left:442px;top:779px;width:350px"><strong>Sed ut perspiciatis unde</strong> omnis iste natus error sit voluptatem accusantium doloremque laudantium, totam rem aperiam, eaque ipsa quae ab illo inventore veritatis et quasi architecto</p>
<div class="abs bullet" style="left:444px;top:870px"></div>
<div class="abs teal-link" style="left:467px;top:863px">Sed ut perspiciatis</div>
<div class="abs bullet" style="left:598px;top:870px"></div>
<div class="abs teal-link" style="left:621px;top:863px">Sed ut perspiciatis</div>
<div class="abs photo-frame"><div role="img" aria-label="Photographer holding a camera"></div></div>
<p class="abs body-copy" style="left:559px;top:906px;width:230px"><strong>Sed ut perspiciatis unde</strong> omnis iste natus error sit voluptatem accusantium doloremque laudantium, totam rem aperiam, eaque ipsa quae ab illo</p>
<a class="abs read-more" style="left:681px;top:1024px">Read More &gt;&gt;</a>

<h3 class="abs section-title" style="left:863px;top:727px">USEFUL LINKS</h3>
<ul class="abs links" style="left:901px;top:782px">
  <li style="top:0">Sed ut perspiciatis</li>
  <li style="top:22px">Lorem ipsum</li>
  <li style="top:44px">Dolor sit amet,</li>
  <li style="top:65px">Consectetur</li>
  <li style="top:87px">Adipiscing elit,</li>
  <li style="top:109px">Sed do eiusmod</li>
</ul>
<p class="abs body-copy" style="left:863px;top:932px;width:200px">empor incididunt ut labore et dolore magna aliqua. Ut enim ad minim veniam, quis nostrud</p>
<a class="abs read-more" style="left:971px;top:1027px">Read More &gt;&gt;</a>

<footer>
  <div class="abs footer"></div>
  <div class="abs foot-nav">HOME<span>|</span>ABOUT ME<span>|</span>PORTFOLIO<span>|</span>GALLERY<span>|</span>INVESTMENT<span>|</span>CONTACT US</div>
  <div class="abs copyright">© COPYRIGHT. 2015.PERSONAL PHOTOGRAPHY. ALL RIGHTS RESERVED.</div>
  <div class="abs follow">FOLLOW US :</div>
  <div class="abs social" style="left:886px"></div>
  <div class="abs social" style="left:920px"></div>
  <div class="abs social" style="left:954px"></div>
  <div class="abs social" style="left:988px"></div>
  <div class="abs social" style="left:1022px"></div>
  <div class="abs social" style="left:1056px"></div>
</footer>

</body>
</html>
```